Brom Vela CEO and Partners Business Card

We need a fresh, fun, simple and clean business card design....we would like a template where we can add a name and title (as well as specific email addresses). We are open to different looks (full logo on one side and a small logo on the company info side, or our logo is in the background but faint on one side but full on the other, or something else cool :-) ). Our colors are in our logo: blue, black and white...however we are not opposed to the use of other colors if it works. We build sets, make props and a host of other things for the film and television industry...our card should reflect creativity, style and professionalism.

A white background would be preferred.

I would like to see an option with Facebook and Instagram icons.

Facebook- facebook.com/bromvelaqt
Instagram- brom_vela

Our website is bromvela-example.com.

Brom Vela, Inc.
4168 Tolliver Crescent, Unit 9
Larkmoor Valley, Nevada 89921
555.210.4872 | tel
555.210.6391 | fax
www.BromVela-example.com

Sample Name and Title #1:

Curtis Welbore
CEO / Co-Owner
555.210.4872 | tel
555.210.6391 | fax
curtis@bromvela-example.com
www.BromVela-example.com

Target Market(s)

Marketing Professionals, Production Designers, Interior Designers, Film Producers, Directors, Art Directors, Event Directors

Industry/Entity Type

Entertainment Industry

Contact Information for Business Card

Curtis Welbore
CEO / Co-Owner
555.210.4872 | tel
555.210.6391 | fax
curtis@bromvela-example.com
www.BromVela-example.com

Font styles to use
Sans Serif

Colors
33a6d7
ffffff
1b1b1b

Requirements
Must have
• Logo, All Contact Info, White Background. Symmetry.
Nice to have
• Facebook and Instagram icons with addresses
• Facebook- facebook.com/bromvelaqt
• Instagram- brom_vela

```html
<!DOCTYPE html>
<html lang="en">
<head>
<meta charset="utf-8">
<title>Brom Vela CEO and Partners Business Card</title>
<link rel="stylesheet" href="https://fonts.googleapis.com/css2?family=Open+Sans:wght@400;600;700;800&display=swap">
<style>
  :root {
    --brand-blue: #33a6d7;
    --brand-black: #1b1b1b;
    --brand-white: #ffffff;
    --backdrop: #e9e6e3;
  }
  * { box-sizing: border-box; margin: 0; padding: 0; }
  html, body { width: 1171px; height: 1200px; overflow: hidden; }
  body {
    background: var(--backdrop);
    font-family: "Open Sans", Arial, sans-serif;
    color: var(--brand-black);
    position: relative;
  }
  .card {
    position: absolute;
    left: 85px;
    width: 1000px;
    height: 560px;
    background: var(--brand-white);
    box-shadow: 0 6px 24px rgba(0,0,0,0.15);
    overflow: hidden;
  }
  .card--front { top: 30px; }
  .card--back { top: 615px; }

  .wordmark {
    position: absolute;
    font-weight: 800;
    color: var(--brand-black);
    letter-spacing: -1px;
    white-space: nowrap;
    line-height: 1;
  }
  .card--front .wordmark { left: 250px; top: 85px; font-size: 62px; }
  .card--back .wordmark { left: 470px; top: 245px; font-size: 82px; }

  .info-band {
    position: absolute;
    left: 180px; right: 0;
    top: 185px; height: 285px;
    background: var(--brand-blue);
    color: var(--brand-black);
  }
  .person { position: absolute; left: 80px; top: 26px; }
  .person__name { font-size: 30px; font-weight: 700; line-height: 1.1; }
  .person__title { font-size: 20px; font-weight: 400; margin-top: 4px; }

  .contact-list {
    position: absolute; left: 80px; top: 120px;
    list-style: none; font-size: 20px; line-height: 1.3;
  }
  .contact-list li { display: flex; align-items: flex-start; gap: 14px; }
  .contact-list svg { width: 18px; height: 18px; margin-top: 4px; flex: none; }

  .social-list {
    position: absolute; left: 560px; top: 120px;
    list-style: none; font-size: 20px; line-height: 1.3;
  }
  .social-list li { display: flex; align-items: center; gap: 12px; margin-bottom: 12px; }
  .social-mark {
    width: 16px; height: 16px; background: var(--brand-black); border-radius: 3px; flex: none;
  }

  .accent-block {
    position: absolute; left: 0; top: 110px;
    width: 150px; height: 340px;
    background: var(--brand-blue);
  }
</style>
</head>
<body>
  <section class="card card--front" aria-label="Business card front">
    <div class="wordmark">BROM VELA</div>
    <div class="info-band">
      <div class="person">
        <div class="person__name">Curtis Welbore</div>
        <div class="person__title">CEO / Co-Owner</div>
      </div>
      <ul class="contact-list">
        <li>
          <svg viewBox="0 0 24 24" aria-hidden="true"><path fill="#1b1b1b" d="M6.6 10.8a15 15 0 0 0 6.6 6.6l2.2-2.2c.3-.3.7-.4 1-.2 1.1.4 2.3.6 3.6.6.6 0 1 .4 1 1V20c0 .6-.4 1-1 1A17 17 0 0 1 3 4c0-.6.4-1 1-1h3.5c.6 0 1 .4 1 1 0 1.3.2 2.5.6 3.6.1.3 0 .7-.2 1z"/></svg>
          <span>555.210.4872</span>
        </li>
        <li>
          <svg viewBox="0 0 24 24" aria-hidden="true"><rect x="3" y="8" width="18" height="12" rx="2" fill="#1b1b1b"/><rect x="7" y="3" width="10" height="6" fill="#1b1b1b"/><rect x="7" y="12" width="10" height="2" fill="#33a6d7"/></svg>
          <span>555.210.6391</span>
        </li>
        <li>
          <svg viewBox="0 0 24 24" aria-hidden="true"><rect x="2" y="5" width="20" height="14" rx="1" fill="#1b1b1b"/><path d="M2 6l10 7 10-7" fill="none" stroke="#33a6d7" stroke-width="2"/></svg>
          <span>curtis@bromvela-example.com</span>
        </li>
        <li>
          <svg viewBox="0 0 24 24" aria-hidden="true"><circle cx="12" cy="12" r="9" fill="none" stroke="#1b1b1b" stroke-width="2"/><path d="M3 12h18M12 3c3 3 3 15 0 18M12 3c-3 3-3 15 0 18" fill="none" stroke="#1b1b1b" stroke-width="2"/></svg>
          <span>www.BromVela-example.com</span>
        </li>
        <li>
          <svg viewBox="0 0 24 24" aria-hidden="true"><path fill="#1b1b1b" d="M12 2a7 7 0 0 0-7 7c0 5 7 13 7 13s7-8 7-13a7 7 0 0 0-7-7zm0 9.5A2.5 2.5 0 1 1 12 6.5a2.5 2.5 0 0 1 0 5z"/></svg>
          <span>4168 Tolliver Crescent, Unit 9<br>Larkmoor Valley, Nevada 89921</span>
        </li>
      </ul>
      <ul class="social-list">
        <li><span class="social-mark" aria-hidden="true"></span><span>bromvelaqt</span></li>
        <li><span class="social-mark" aria-hidden="true"></span><span>brom_vela</span></li>
      </ul>
    </div>
  </section>

  <section class="card card--back" aria-label="Business card back">
    <div class="accent-block"></div>
    <div class="wordmark">BROM VELA</div>
  </section>
</body>
</html>
```